Aged Care Consultancy Business needs a business card design

I need a two sided business card - I want it clean and professional. Surprise me

Target Market(s)

middle aged and ageing victorians

Industry/Entity Type

Health Care

Contact Information for Business Card

Text to be included

Logo
Aged Care Consulting Services
Professional, Reliable, Affordable

Tovan Brelsick
Director
0427 31 64 92 (larger)
1300 73 29 41
tovan@wadolire.com.au
www.wadolcare.com.au
Facebook (details TBA)

include little icons beside the contact info:

- Envelope = email
- Phone = phone
- Globe = website

Font styles to use
Serif
Sans Serif

Requirements
Must have
• look proffesional and clean

```html
<!DOCTYPE html>
<html lang="en">
<head>
<meta charset="utf-8">
<title>Wadol Care – Business Card</title>
<link href="https://fonts.googleapis.com/css2?family=Open+Sans:wght@400;600;700&display=swap" rel="stylesheet">
<style>
  :root {
    --navy: #123f83;
    --amber: #e8960f;
    --ink: #1d1d1d;
    --paper: #ffffff;
    --backdrop: #c9c9c9;
    --rule: #2b4f8f;
  }
  * { box-sizing: border-box; margin: 0; padding: 0; }
  html, body { width: 1200px; height: 1200px; overflow: hidden; }
  body {
    background: var(--backdrop);
    font-family: "Open Sans", sans-serif;
    color: var(--ink);
    position: relative;
  }
  .card {
    position: absolute;
    left: 180px;
    width: 840px;
    height: 480px;
    background: var(--paper);
    box-shadow: 0 6px 18px rgba(0,0,0,0.18);
  }
  .card--front { top: 90px; }
  .card--back { top: 630px; }

  /* Front */
  .brand {
    position: absolute;
    left: 420px;
    top: 90px;
    display: flex;
    align-items: center;
    gap: 16px;
  }
  .brand__dot {
    width: 44px; height: 44px;
    border-radius: 50%;
    background: var(--amber);
  }
  .brand__name {
    font-size: 58px;
    font-weight: 700;
    color: var(--navy);
    letter-spacing: -0.5px;
    line-height: 1;
  }
  .tagline {
    position: absolute;
    left: 430px;
    top: 222px;
    width: 330px;
    font-size: 22px;
    color: var(--navy);
    padding-bottom: 8px;
    border-bottom: 1px solid var(--rule);
  }
  .values {
    position: absolute;
    left: 440px;
    top: 282px;
    list-style: none;
    font-size: 18px;
    line-height: 32px;
    color: var(--ink);
  }

  /* Back */
  .person {
    position: absolute;
    left: 400px;
    top: 60px;
  }
  .person__name {
    font-size: 46px;
    font-weight: 600;
    color: var(--navy);
    line-height: 1.1;
  }
  .person__role {
    font-size: 22px;
    margin-top: 2px;
  }
  .person__mobile {
    font-size: 25px;
    margin-top: 4px;
  }
  .contact {
    position: absolute;
    left: 500px;
    top: 236px;
    width: 300px;
    border-top: 1px solid var(--rule);
    padding-top: 12px;
    list-style: none;
  }
  .contact__item {
    display: flex;
    align-items: center;
    gap: 14px;
    font-size: 18px;
    height: 36px;
  }
  .contact__icon {
    width: 24px; height: 24px;
    flex: none;
    stroke: var(--navy);
    fill: none;
    stroke-width: 1.5;
  }
</style>
</head>
<body>

<section class="card card--front" aria-label="Front of business card">
  <div class="brand">
    <span class="brand__dot"></span>
    <span class="brand__name">wadol care</span>
  </div>
  <p class="tagline">Aged Care Consulting Services</p>
  <ul class="values">
    <li>Professional</li>
    <li>Reliable</li>
    <li>Affordable</li>
  </ul>
</section>

<section class="card card--back" aria-label="Back of business card">
  <div class="person">
    <h1 class="person__name">Tovan Brelsick</h1>
    <p class="person__role">Director</p>
    <p class="person__mobile">0427 31 64 92</p>
  </div>
  <ul class="contact">
    <li class="contact__item">
      <svg class="contact__icon" viewBox="0 0 24 24" aria-hidden="true">
        <path d="M5 3h4l2 5-2.5 1.5a11 11 0 0 0 6 6L16 13l5 2v4a2 2 0 0 1-2 2A16 16 0 0 1 3 5a2 2 0 0 1 2-2z"/>
      </svg>
      <span>1300 73 29 41</span>
    </li>
    <li class="contact__item">
      <svg class="contact__icon" viewBox="0 0 24 24" aria-hidden="true">
        <rect x="2" y="5" width="20" height="14"/>
        <path d="M2 5l10 8 10-8M2 19l7-7M22 19l-7-7"/>
      </svg>
      <span>tovan@wadolire.com.au</span>
    </li>
    <li class="contact__item">
      <svg class="contact__icon" viewBox="0 0 24 24" aria-hidden="true">
        <circle cx="12" cy="12" r="10"/>
        <ellipse cx="12" cy="12" rx="4.5" ry="10"/>
        <path d="M2 12h20M4 7h16M4 17h16"/>
      </svg>
      <span>www.wadolcare.com.au</span>
    </li>
    <li class="contact__item">
      <svg class="contact__icon" viewBox="0 0 24 24" aria-hidden="true">
        <circle cx="12" cy="12" r="10"/>
      </svg>
      <span>name/face.book</span>
    </li>
  </ul>
</section>

</body>
</html>
```